Kelpfair 2021 30th Anniversary

I need a graphic designer to create our event collateral. Including A3 poster design, DL flyer design , social media tiles (instagram and FB) and web banner. Kelpfair is celebrating it's 30th year anniversary. The event will be held Fri 1 Oct - Sunday 3rd Oct 2021. The council is located in the Eyre Peninsula in South Australia. We are known for our world class Oysters. I have attached an old poster from previous years. I want to really modernise the design. The A3 poster design will need to be able to be amended so I can continue to add sponsorship logos. Link to FB for further information on the event https://www.pagebook.example/MarrowinKelpfair. I have included the current Kelpfair logo and Council logo. A poster from 2018 has been included. I am not looking to include any images from previous events. I want a completely new design, bright in colour to attract readers to print advertisements etc I have also attached a design which we had a bit of a play with ourselves but are looking for a more professional design.

Brief - 30th Anniversary Friday 1st October – Sunday 3rd 2021
- Shellfish Harbour of the South
- World Class Oyster’s and Specialty Cuisines
- Premier Wine, Craft Beers & Cocktails
- Live Entertainment
- Side Show Alley
- Kid’s Corner
- Artisan markets
- Fireworks display
- Social media handles FB: @MarrowinKelpfair
Insta: @MarrowinKelpFair

Requirements
Must have
• Social media handles
Dates of event
Ability to amend sponsorship/add sponsorship logos
Bright colours
Fit the profile of the region (seaside, seafood etc)
Nice to have
• Colour scheme similar to Kelpfair logo provided

```html
<!DOCTYPE html>
<html lang="en">
<head>
<meta charset="utf-8">
<title>Kelpfair Marrowin 2021 – 30th Anniversary</title>
<link rel="stylesheet" href="https://fonts.googleapis.com/css2?family=Montserrat:wght@500;600;700;800&family=Playball&display=swap">
<style>
  :root {
    --orange: #e9572b;
    --orange-deep: #d9461f;
    --sea-top: #5fa2c7;
    --sea-mid: #3f7fae;
    --sea-low: #2c5f8c;
    --white: #ffffff;
    --ink: #333a45;
    --grey: #8a8f96;
    --sun: #f4c21b;
    --footer: #f1f1f1;
  }
  * { box-sizing: border-box; margin: 0; padding: 0; }
  html, body { width: 849px; height: 1200px; overflow: hidden; background: var(--white); }
  body { font-family: "Montserrat", sans-serif; color: var(--ink); }

  .poster { position: relative; width: 849px; height: 1200px; overflow: hidden; background: var(--white); }

  /* header */
  .masthead { position: absolute; top: 0; left: 0; width: 849px; height: 62px; display: flex; justify-content: space-between; align-items: center; padding: 0 26px; }
  .event-mark { display: flex; align-items: center; gap: 8px; font-weight: 800; font-size: 24px; color: var(--orange); letter-spacing: 0.5px; }
  .event-mark .dot { width: 20px; height: 20px; border-radius: 50%; background: var(--orange); }
  .council-mark { display: flex; align-items: center; gap: 8px; font-weight: 600; font-size: 11px; color: var(--sea-low); line-height: 1.2; }
  .council-mark .dot { width: 30px; height: 30px; border-radius: 50%; background: var(--sun); }

  /* orange hero band */
  .hero { position: absolute; top: 62px; left: 0; width: 849px; height: 490px; background: var(--orange); }
  .hero-photo { position: absolute; left: 62px; top: 57px; width: 322px; height: 362px; background: radial-gradient(circle at 45% 50%, #efe9df 0%, #d8cfc2 45%, #b9ab99 100%); }
  .hero-copy { position: absolute; left: 420px; top: 40px; width: 390px; color: var(--white); text-align: center; }
  .anniversary { font-weight: 800; font-size: 34px; line-height: 1.05; letter-spacing: 0.5px; }
  .anniversary sup { font-size: 16px; vertical-align: top; position: relative; top: 4px; }
  .dates { font-weight: 800; font-size: 34px; line-height: 1.1; }
  .tagline-script { font-family: "Playball", cursive; font-size: 52px; line-height: 1; margin-top: 62px; }
  .tagline-caps { font-weight: 600; font-size: 26px; letter-spacing: 1px; margin-top: 2px; }
  .tagline-sub { font-weight: 600; font-size: 18px; letter-spacing: 0.5px; line-height: 1.35; margin-top: 70px; }

  /* sea band with features */
  .features { position: absolute; top: 552px; left: 0; width: 849px; height: 298px; }
  .features-bg { position: absolute; inset: 0; background: linear-gradient(180deg, var(--sea-top) 0%, var(--sea-mid) 55%, var(--sea-low) 100%); }
  .feature-grid { position: absolute; left: 136px; top: 22px; display: grid; grid-template-columns: 266px 266px; column-gap: 45px; row-gap: 14px; }
  .feature { height: 78px; border: 2px solid var(--white); display: flex; align-items: center; justify-content: center; text-align: center; color: var(--white); font-weight: 700; font-size: 17px; letter-spacing: 0.5px; line-height: 1.3; padding: 0 12px; }

  /* sponsors */
  .sponsors { position: absolute; top: 880px; left: 40px; width: 769px; }
  .sponsor-row { display: flex; justify-content: space-between; align-items: center; height: 66px; margin-bottom: 24px; }
  .sponsor { height: 34px; border-radius: 3px; }

  /* footer */
  .footer { position: absolute; bottom: 0; left: 0; width: 849px; height: 54px; background: var(--footer); display: flex; align-items: center; justify-content: space-between; padding: 0 26px; font-size: 13px; font-weight: 500; color: var(--ink); }
  .socials { display: flex; gap: 26px; }
  .social { display: flex; align-items: center; gap: 7px; }
  .social .dot { width: 18px; height: 18px; border-radius: 50%; background: var(--grey); }
</style>
</head>
<body>
<main class="poster">
  <header class="masthead">
    <div class="event-mark"><span class="dot"></span>Kelpfair Marrowin</div>
    <div class="council-mark"><span class="dot"></span><span>District Council<br>of Marrowin</span></div>
  </header>

  <section class="hero">
    <div class="hero-photo" role="img" aria-label="Photo of fresh oysters on a white plate with a dipping sauce"></div>
    <div class="hero-copy">
      <p class="anniversary">30<sup>TH</sup> ANNIVERSARY</p>
      <p class="dates">OCTOBER 1-3, 2021</p>
      <h1 class="tagline-script">Shellfish Harbour</h1>
      <p class="tagline-caps">OF THE SOUTH</p>
      <p class="tagline-sub">WORLD CLASS OYSTERS AND<br>SPECIALTY CUISINES</p>
    </div>
  </section>

  <section class="features">
    <div class="features-bg" role="img" aria-label="Photo of a calm blue sea with a long jetty at dusk"></div>
    <div class="feature-grid">
      <div class="feature">PREMIER WINE, CRAFT<br>BEERS, AND COCKTAILS</div>
      <div class="feature">KID'S CORNER</div>
      <div class="feature">ARTISAN MARKET</div>
      <div class="feature">SIDE SHOW ALLEY</div>
      <div class="feature">LIVE ENTERTAINMENT</div>
      <div class="feature">FIREWORKS DISPLAY</div>
    </div>
  </section>

  <section class="sponsors" aria-label="Sponsors">
    <div class="sponsor-row">
      <span class="sponsor" style="width:110px;background:#c8282e"></span>
      <span class="sponsor" style="width:70px;background:#2e7d3a"></span>
      <span class="sponsor" style="width:40px;background:#e03a2f"></span>
      <span class="sponsor" style="width:50px;background:#f0b323"></span>
      <span class="sponsor" style="width:60px;background:#d62828"></span>
      <span class="sponsor" style="width:80px;background:#9aa3ad"></span>
      <span class="sponsor" style="width:60px;background:#6b8fb5"></span>
      <span class="sponsor" style="width:80px;background:#1d4f91"></span>
    </div>
    <div class="sponsor-row">
      <span class="sponsor" style="width:30px;background:#1d3a6b"></span>
      <span class="sponsor" style="width:52px;background:#1d3a6b"></span>
      <span class="sponsor" style="width:70px;background:#d63b2f"></span>
      <span class="sponsor" style="width:60px;background:#4a90c8"></span>
      <span class="sponsor" style="width:70px;background:#2b2b2b"></span>
      <span class="sponsor" style="width:70px;background:#e85d2a"></span>
      <span class="sponsor" style="width:70px;background:#7aa7c7"></span>
      <span class="sponsor" style="width:70px;background:#4c9a5b"></span>
      <span class="sponsor" style="width:55px;background:#d4a21c"></span>
      <span class="sponsor" style="width:60px;background:#e0902a"></span>
    </div>
    <div class="sponsor-row">
      <span class="sponsor" style="width:56px;background:#e8552b"></span>
      <span class="sponsor" style="width:60px;background:#2d6fb5"></span>
      <span class="sponsor" style="width:56px;background:#3c8fc4"></span>
      <span class="sponsor" style="width:56px;background:#6e7b8a"></span>
      <span class="sponsor" style="width:56px;background:#2e5c8a"></span>
      <span class="sponsor" style="width:40px;background:#4aa04a"></span>
      <span class="sponsor" style="width:50px;background:#c23a3a"></span>
      <span class="sponsor" style="width:60px;background:#f3c8cf"></span>
      <span class="sponsor" style="width:70px;background:#3b6fa5"></span>
      <span class="sponsor" style="width:56px;background:#2f8a8a"></span>
    </div>
  </section>

  <footer class="footer">
    <p>Tickets available via www.ticketbay.example/</p>
    <div class="socials">
      <span class="social"><span class="dot"></span>@MarrowinKelpfair</span>
      <span class="social"><span class="dot"></span>@MarrowinKelpfair</span>
    </div>
  </footer>
</main>
</body>
</html>
```